Business Card For Talent Company
BLITZ Talent
Project: Business Card For Talent Company
Business Card For Talent Company - Entertainment
Creative Brief
Cutting-Edge
Lorna Pidge
Talent Development
2734 W. Ferncastle Rd. Dovermill Park IL 60419
blitztalent@quorvex.com
www.blitztalent-quorvex.com
Are you ready to break through?
Kelvorn Kelvorn
We are really desperate to see some fun contemporary and modern designs...we are a talent company...would really like to see something innovative and not so corporate looking.....thank you!
Aquamarine/Teal Shade of Blue Please!....We really want something fun and edgy....these are too corporate looking...
We are a talent agency....really looking for something cool and cutting edge for our company...the shade of blue is coming through wrong on the logo...we are looking for a more like a teal blue color....thank you!
Our Tag Line "are you ready to break through" needs to be on all of the materials....thank you!
we are looking for more of teal shade of blue..I uploaded our other logo....
This contest is for full stationary...
It is both business card and stationary that we are needing....thank you!

```html
<!DOCTYPE html>
<html lang="en">
<head>
<meta charset="utf-8">
<title>BLITZ Talent — Stationery Set</title>
<link href="https://fonts.googleapis.com/css2?family=Michroma&family=Open+Sans:wght@400;600&display=swap" rel="stylesheet">
<style>
  :root{
    --ground:#e7e4df;
    --paper:#ffffff;
    --ink:#111111;
    --band:#0d0d0d;
    --muted:#8a8a8a;
    --rule:#c9c9c9;
    --teal-deep:#1d3f8a;
    --teal-mid:#3a6fc2;
    --violet:#4a3d9c;
    --label:#333333;
  }
  *{box-sizing:border-box;margin:0;padding:0}
  html,body{width:1200px;height:343px;overflow:hidden;background:var(--ground)}
  body{position:relative;font-family:"Open Sans",Arial,sans-serif;color:var(--ink)}
  .wordmark{font-family:"Michroma",Arial,sans-serif;letter-spacing:1px;color:var(--paper)}

  .sheet{position:absolute;top:19px;width:271px;height:293px;background:var(--paper);box-shadow:0 2px 6px rgba(0,0,0,.18)}
  .sheet--one{left:12px}
  .sheet--two{left:307px}
  .sheet--fax{left:602px}
  .sheet__head{height:30px;background:var(--band);display:flex;align-items:center;justify-content:space-between;padding:0 12px}
  .sheet__head .wordmark{font-size:11px}
  .sheet__contact{font-size:3.6px;line-height:5px;color:#cfcfcf;text-align:right}
  .sheet__foot{position:absolute;bottom:8px;left:0;right:0;text-align:center;font-size:4.2px;letter-spacing:1px;color:var(--muted);text-transform:uppercase}
  .sheet__foot--bar{bottom:0;height:9px;padding-top:2px;background:var(--band);color:#bdbdbd}

  .option-label{position:absolute;top:317px;font-size:11px;color:var(--label);width:271px;text-align:center}

  .fax__title{position:absolute;top:44px;left:16px;font-size:16px;font-weight:600;letter-spacing:1px}
  .fax__fields{position:absolute;top:70px;left:16px;right:16px;display:grid;grid-template-columns:1fr 1fr;column-gap:14px;row-gap:7px}
  .fax__field{display:flex;align-items:flex-end;font-size:5px;color:var(--label)}
  .fax__field span{width:18px}
  .fax__field i{flex:1;border-bottom:.6px solid var(--rule);height:6px}
  .fax__checks{position:absolute;top:108px;left:16px;right:16px;display:flex;justify-content:space-between;font-size:4.6px;color:var(--label)}
  .fax__checks span::before{content:"";display:inline-block;width:4px;height:4px;border:.6px solid var(--label);margin-right:2px;vertical-align:-1px}
  .fax__rule{position:absolute;top:120px;left:16px;right:16px;border-top:.8px solid var(--rule)}

  .envelope{position:absolute;width:240px;height:104px;box-shadow:0 2px 5px rgba(0,0,0,.2)}
  .envelope svg{position:absolute;inset:0}
  .envelope--back{left:900px;top:12px;background:linear-gradient(135deg,var(--violet),var(--teal-mid))}
  .envelope--dark{left:953px;top:30px;background:var(--band)}
  .envelope--front{left:900px;top:120px;width:175px;height:78px;background:var(--paper)}
  .envelope__band{position:absolute;left:0;right:0;top:30px;height:16px;background:var(--band);display:flex;align-items:center;padding-left:10px}
  .envelope__band .wordmark{font-size:8px}
  .envelope__seal{position:absolute;left:50%;top:34px;transform:translateX(-50%);font-size:8px}

  .card{position:absolute;top:233px;width:138px;height:79px;box-shadow:0 2px 5px rgba(0,0,0,.25);padding:12px}
  .card--dark{left:900px;background:var(--band)}
  .card--teal{left:1052px;background:linear-gradient(135deg,var(--teal-deep),var(--teal-mid));display:flex;align-items:center;justify-content:center}
  .card .wordmark{font-size:14px}
  .card__name{position:absolute;left:12px;bottom:16px;font-size:5.5px;font-weight:600;color:var(--paper)}
  .card__title{position:absolute;left:12px;bottom:9px;font-size:4.2px;color:#bcbcbc}
  .card__strip{position:absolute;left:0;right:0;bottom:0;height:5px;background:var(--teal-mid)}
</style>
</head>
<body>

<section class="sheet sheet--one">
  <header class="sheet__head">
    <span class="wordmark">BLITZ</span>
    <div class="sheet__contact">2734 W. Ferncastle Rd. Dovermill Park IL 60419<br>blitztalent@quorvex.com</div>
  </header>
  <footer class="sheet__foot">Are you ready to break through? · www.blitztalent-quorvex.com</footer>
</section>
<div class="option-label" style="left:12px">Option-1</div>

<section class="sheet sheet--two">
  <header class="sheet__head">
    <span class="wordmark">BLITZ</span>
    <div class="sheet__contact">2734 W. Ferncastle Rd.<br>Dovermill Park IL 60419<br>blitztalent@quorvex.com<br>www.blitztalent-quorvex.com</div>
  </header>
  <footer class="sheet__foot sheet__foot--bar">Are you ready to break through?</footer>
</section>
<div class="option-label" style="left:307px">Option-2</div>

<section class="sheet sheet--fax">
  <header class="sheet__head">
    <span class="wordmark">BLITZ</span>
    <div class="sheet__contact">blitztalent@quorvex.com<br>www.blitztalent-quorvex.com</div>
  </header>
  <h1 class="fax__title">FAX</h1>
  <div class="fax__fields">
    <div class="fax__field"><span>To:</span><i></i></div>
    <div class="fax__field"><span>From:</span><i></i></div>
    <div class="fax__field"><span>Fax:</span><i></i></div>
    <div class="fax__field"><span>Phone:</span><i></i></div>
    <div class="fax__field"><span>Date:</span><i></i></div>
    <div class="fax__field"><span>Pages:</span><i></i></div>
  </div>
  <div class="fax__checks">
    <span>Urgent</span><span>Review</span><span>Comment</span><span>Reply</span><span>Recycle</span>
  </div>
  <div class="fax__rule"></div>
  <footer class="sheet__foot">2734 W. Ferncastle Rd. Dovermill Park IL 60419</footer>
</section>
<div class="option-label" style="left:602px">Option-3</div>

<div class="envelope envelope--back">
  <svg viewBox="0 0 240 104" preserveAspectRatio="none"><path d="M0 0 L120 52 L240 0" fill="none" stroke="rgba(255,255,255,.35)" stroke-width="1"/></svg>
</div>
<div class="envelope envelope--dark">
  <svg viewBox="0 0 240 104" preserveAspectRatio="none"><path d="M0 0 L120 56 L240 0 Z" fill="#1c1c1c"/></svg>
  <span class="wordmark envelope__seal">BLITZ</span>
</div>
<div class="envelope envelope--front">
  <div class="envelope__band"><span class="wordmark">BLITZ</span></div>
</div>

<div class="card card--dark">
  <span class="wordmark">BLITZ</span>
  <div class="card__name">Lorna Pidge</div>
  <div class="card__title">Talent Development</div>
  <div class="card__strip"></div>
</div>
<div class="card card--teal">
  <span class="wordmark">BLITZ</span>
</div>

</body>
</html>
```